Maple Sprout Menu (Vegetarian Restaurant Concept)

Maple Sprout is a new concept fast casual restaurant
renders are attached so you can see the style of restaurant
Maple Sproutt is a vibrant and modern Vegetarian fast casual restaurant concept that mixes fresh food, energy, great décor, and a comfortable, welcoming atmosphere to provide a memorable and all Vegetarian dining experience.
Our Mission is to be top of mind when consumers think Vegetarian food!
Target Market(s)
the menu is vegetarian and appeals to a broad demographic in USA
Colors
Designer to choose colors to be used in the design.
Requirements
Must have
- well colored and well laid out menu - should not be cartoonish
Nice to have
- For Phots please use the shots in this file:
- https://www.filecrate-example.com/sh/qwx7tr2bnm4kdle/BBBdK_pQrLmNZTHO5E_XYZ_Kb?dl=0
- note these are untouched and you are free to change as needed
Should not have
- Should not be cartoonish - nor kives, forks etc in the design

```html
<!DOCTYPE html>
<html lang="en">
<head>
<meta charset="utf-8">
<title>Maple Sprout Menu</title>
<link rel="stylesheet" href="https://fonts.googleapis.com/css2?family=Exo:wght@800&family=Merriweather:wght@400;700&display=swap">
<style>
  :root {
    --wood-dark: #3b2419;
    --wood-mid: #5a3825;
    --wood-light: #6e4630;
    --leaf: #7cc043;
    --panel: #79b54a;
    --panel-ink: #17220f;
    --cream: #f4efe6;
    --bowl: #e6dcc6;
    --heading-font: "Exo", "Arial Black", sans-serif;
    --body-font: "Merriweather", Georgia, serif;
  }
  * { margin: 0; padding: 0; box-sizing: border-box; }
  html, body { width: 848px; height: 1200px; overflow: hidden; }
  body { background: var(--wood-dark); }
  .menu {
    position: relative; width: 848px; height: 1200px; overflow: hidden;
    background: linear-gradient(90deg, var(--wood-dark) 0%, var(--wood-mid) 30%, var(--wood-light) 50%, var(--wood-mid) 70%, var(--wood-dark) 100%);
    font-family: var(--body-font); color: var(--cream);
  }
  .abs { position: absolute; }
  .section-title {
    position: absolute; font-family: var(--heading-font); font-weight: 800;
    color: var(--leaf); font-size: 35px; line-height: 1; letter-spacing: 0.2px;
  }
  .item { position: absolute; font-size: 16px; line-height: 19px; }
  .item-name { font-weight: 700; display: block; }
  .item-desc { font-weight: 400; display: block; }
  .photo { position: absolute; border-radius: 50%; }
  .panel { position: absolute; background: var(--panel); color: var(--panel-ink); }
  .panel .item { font-size: 18.5px; line-height: 24px; }
  .dessert .item { font-size: 16.5px; line-height: 17px; }
</style>
</head>
<body>
<main class="menu">

  <div class="photo" role="img" aria-label="Photo of a veggie wrap cut in half in a paper bowl"
       style="left:434px; top:-78px; width:420px; height:340px; background: radial-gradient(circle at 50% 55%, #c9d38c 0%, #e8dcbf 45%, var(--bowl) 70%);"></div>

  <div class="photo" role="img" aria-label="Photo of a green salad with avocado, cherry tomatoes, almonds and goat cheese in a paper bowl"
       style="left:0; top:403px; width:350px; height:312px; background: radial-gradient(circle, #5e7f33 0%, #7a8a3e 45%, #8f6e3d 62%, var(--bowl) 70%);"></div>

  <div class="photo" role="img" aria-label="Photo of a strawberry balsamic ice cream sundae in a clear cup"
       style="left:-10px; top:954px; width:236px; height:300px; border-radius: 40% 40% 0 0; background: radial-gradient(circle at 50% 45%, #b23a2e 0%, #d8c7a6 50%, #c9c3b8 75%);"></div>

  <div class="photo" role="img" aria-label="Photo of tomato and beet bruschetta topped with basil in a paper bowl"
       style="left:548px; top:930px; width:400px; height:340px; background: radial-gradient(circle at 55% 60%, #7e1e2c 0%, #8a2a35 40%, var(--bowl) 64%);"></div>

  <h2 class="section-title" style="left:38px; top:31px;">SALADS</h2>
  <p class="item" style="left:38px; top:82px;"><span class="item-name">Brussel Sprout Ceasar</span><span class="item-desc">little gem romaine, toasted torn bread,<br>parmigiano reggiano</span></p>
  <p class="item" style="left:38px; top:159px;"><span class="item-name">Heirloom Beet salad</span><span class="item-desc">shaved chioggia beet, roasted golden beet, red<br>quinoa, little gem, arugula, lemon vinaigrette</span></p>
  <p class="item" style="left:38px; top:235px;"><span class="item-name">Zesty Black Bean and Corn Salad in lettuce<br>cups</span><span class="item-desc">black beans, avocado and roasted corn topped<br>with feta crumbles in butter lettuce</span></p>
  <p class="item" style="left:38px; top:330px;"><span class="item-name">Green, Red and White</span><span class="item-desc">spring leaves, cherry tomatoes, avocado,<br>roasted almond and goat cheese</span></p>

  <h2 class="section-title" style="left:431px; top:270px; font-size:40px; line-height:35px;">BURGERS, WRAPS &amp;<br>SANDWICHES</h2>
  <section class="panel" style="left:416px; top:345px; width:432px; height:420px;">
    <p class="item" style="left:15px; top:27px;"><span class="item-name">Sweet Potato, black bean veggie burgers</span><span class="item-desc">with cabbage - pepita slaw</span></p>
    <p class="item" style="left:15px; top:100px;"><span class="item-name">Roasted Vejjie, Arugula and Hummus<br>Wraps</span></p>
    <p class="item" style="left:15px; top:155px;"><span class="item-name">Garden Burger</span></p>
    <p class="item" style="left:15px; top:190px;"><span class="item-name">Beans and Greens Quesadillas</span><span class="item-desc">greens, Mexican cheese, beans and avocado,<br>with salsa</span></p>
    <p class="item" style="left:15px; top:288px;"><span class="item-name">Vejjie Burrito</span><span class="item-desc">greens, Mexican cheese, beans, brown rice,<br>roasted chili corn and avocado, with ancho<br>chili salsa, wheat tortilla</span></p>
  </section>

  <h2 class="section-title" style="left:38px; top:737px;">TOASTS</h2>
  <p class="item" style="left:25px; top:791px; font-size:17px; line-height:20px;"><span class="item-name">Everything Avocado toast</span><span class="item-desc">avocado on whole grain toast<br>with our signature spice blend</span></p>
  <p class="item" style="left:25px; top:862px; font-size:17px;"><span class="item-name">Tomato &amp; Beet Bruschetta</span></p>
  <p class="item" style="left:25px; top:897px; font-size:17px;"><span class="item-name">Vegetable Melt on garlic Toast</span></p>

  <h2 class="section-title" style="left:432px; top:783px;">BOWLS</h2>
  <p class="item" style="left:427px; top:827px; font-size:17px;"><span class="item-name">Roasted vegetable, and spinach bowl</span></p>
  <p class="item" style="left:427px; top:857px; font-size:17px;"><span class="item-name">Sugar Snap Pea and Carrot Soba Noodles</span></p>
  <p class="item" style="left:427px; top:886px; font-size:17px;"><span class="item-name">Whole grain and vegetable buddha bowl</span></p>
  <p class="item" style="left:427px; top:916px; font-size:17px;"><span class="item-name">Orange and Pistacio Quinoa</span></p>

  <h2 class="section-title" style="left:248px; top:944px;">SOUP</h2>
  <p class="item" style="left:248px; top:978px; font-size:17px;"><span class="item-name">Black Bean Chowder</span></p>

  <h2 class="section-title" style="left:248px; top:1026px;">DESSERT</h2>
  <section class="panel dessert" style="left:226px; top:1064px; width:317px; height:136px;">
    <p class="item" style="left:22px; top:24px;"><span class="item-name">Strawberry Balsamic Ice Cream<br>sundae</span></p>
    <p class="item" style="left:22px; top:70px;"><span class="item-name">Exotic fruit bowl</span></p>
    <p class="item" style="left:22px; top:104px;"><span class="item-name">White and dark oatmeal cookie</span></p>
  </section>

</main>
</body>
</html>
```